We need a business card design for our website rvkventures.com. The Star Headline is rvkventures.com, in large lettering.We sell fashion rings of titanium, mirror pollished stainless steel, and related jewelry. Basically quality products competing with the high expense of gold.We have to portray honesty and trust, because thats who I am. I know marketing, but I am weak on colors and layout. 3D Gold curved edge letters are ok. No green and yellow.Black,Red,Purple and White in small amounts.No fancy Lettering.
No Rainbows in printing.
Our goal is selling our products online globally

Kind Regards Corwin Albury

Fashion

rvkventures.com
known for our ideal fit rings
email.corwinalburyptyltd@fernmail com

```html
<!DOCTYPE html>
<html lang="en">
<head>
<meta charset="utf-8">
<title>RVK Ventures – Business Card</title>
<link rel="stylesheet" href="https://fonts.googleapis.com/css2?family=Cinzel:wght@700&family=Questrial&family=Arimo:wght@700&display=swap">
<style>
  :root {
    --card-black: #000000;
    --ink-white: #ffffff;
    --ribbon-purple: #4b3a9a;
    --ribbon-violet: #6a3fa8;
    --ribbon-glow: rgba(201, 196, 230, 0.35);
  }
  html, body {
    margin: 0;
    padding: 0;
    width: 1200px;
    height: 741px;
    overflow: hidden;
    background: var(--card-black);
  }
  .card {
    position: relative;
    width: 1200px;
    height: 741px;
    background: var(--card-black);
    color: var(--ink-white);
    overflow: hidden;
  }
  .brand-name {
    position: absolute;
    top: 152px;
    left: 0;
    width: 100%;
    margin: 0;
    text-align: center;
    font-family: "Cinzel", serif;
    font-weight: 700;
    font-size: 74px;
    letter-spacing: 3px;
    line-height: 1;
    text-transform: uppercase;
  }
  .tagline {
    position: absolute;
    top: 250px;
    left: 0;
    width: 100%;
    margin: 0;
    text-align: center;
    font-family: "Questrial", sans-serif;
    font-size: 44px;
    letter-spacing: 1.5px;
    line-height: 1;
  }
  .ribbon-area {
    position: absolute;
    left: 0;
    top: 350px;
    width: 1200px;
    height: 220px;
    background:
      radial-gradient(ellipse 70% 38% at 55% 42%, var(--ribbon-purple) 0%, rgba(75, 58, 154, 0.55) 45%, rgba(75, 58, 154, 0) 100%),
      radial-gradient(ellipse 30% 30% at 10% 30%, rgba(75, 58, 154, 0.7) 0%, rgba(75, 58, 154, 0) 100%),
      radial-gradient(ellipse 25% 30% at 95% 55%, rgba(106, 63, 168, 0.75) 0%, rgba(106, 63, 168, 0) 100%),
      radial-gradient(ellipse 80% 50% at 50% 45%, var(--ribbon-glow) 0%, rgba(0, 0, 0, 0) 100%);
  }
  .contact-email {
    position: absolute;
    top: 607px;
    left: 0;
    width: 100%;
    margin: 0;
    text-align: center;
    font-family: "Arimo", sans-serif;
    font-weight: 700;
    font-size: 41px;
    letter-spacing: 1px;
    line-height: 1;
  }
</style>
</head>
<body>
<div class="card">
  <h1 class="brand-name">rvkventures.com</h1>
  <p class="tagline">known for our ideal fit rings</p>

  <div class="ribbon-area" role="img" aria-label="Flowing purple ribbon swooshes with a soft glow across the card"></div>

  <p class="contact-email">corwinalburyptyltd@fernmail.com</p>
</div>
</body>
</html>
```